new roofing company card

New primary business card for roofing company.

Industry/Entity Type

Residential roofing/Specializing in Asphalt and Standing seam metal roofing

Contact Information for Business Card

Phone number is: 555 471 2086 Email: support@halvenshingleworks.example website: www.halvenshingleworks.example

Colors
EB3D1F
EC4F4E
F09395
F8D3D4
FCEDEE

```html
<!DOCTYPE html>
<html lang="en">
<head>
<meta charset="UTF-8">
<title>Halven Shingleworks – Business Card</title>
<link href="https://fonts.googleapis.com/css2?family=Open+Sans:wght@400;700&display=swap" rel="stylesheet">
<style>
  :root {
    --red: #D62E22;
    --red-soft: #EC4F4E;
    --ink: #232323;
    --ink-soft: #4a4a4a;
    --paper: #ffffff;
    --backdrop: #2c2f34;
  }
  * { box-sizing: border-box; margin: 0; padding: 0; }
  html, body {
    width: 1200px; height: 900px; overflow: hidden;
    background: var(--backdrop);
    font-family: "Open Sans", Arial, sans-serif;
  }
  .stage {
    width: 1200px; height: 900px;
    display: flex; flex-direction: column;
    align-items: center; justify-content: center; gap: 40px;
  }
  .card {
    position: relative;
    width: 700px; height: 400px;
    background: var(--paper);
    overflow: hidden;
  }
  .band { position: absolute; width: 34px; background: var(--red); }
  .band--left { left: 0; top: 0; height: 62%; }
  .band--right { right: 0; bottom: 0; height: 74%; }

  .brand {
    color: var(--ink);
    font-weight: 700;
    text-transform: uppercase;
    display: flex; align-items: center; gap: 14px;
    letter-spacing: 0.04em;
  }
  .brand__mark { background: var(--red); flex: none; }

  .card--front .brand { position: absolute; inset: 0; justify-content: center; font-size: 40px; }
  .card--front .brand__mark { width: 26px; height: 26px; }

  .card--back .brand {
    position: absolute; left: 70px; top: 176px; width: 250px;
    font-size: 21px; line-height: 1.1; flex-wrap: nowrap;
  }
  .card--back .brand__mark { width: 18px; height: 18px; }

  .divider {
    position: absolute; left: 330px; top: 110px;
    width: 2px; height: 180px; background: var(--red);
  }
  .contact {
    position: absolute; left: 356px; top: 118px;
    color: var(--ink-soft);
  }
  .contact__name { font-size: 27px; font-weight: 700; color: var(--ink); line-height: 1.15; }
  .contact__name .first { color: var(--red); }
  .contact__role { font-size: 15px; margin: 2px 0 16px; }
  .contact__list { list-style: none; font-size: 14.5px; }
  .contact__list li { display: flex; align-items: center; gap: 10px; margin-bottom: 8px; }
  .contact__list svg { width: 14px; height: 14px; flex: none; }
</style>
</head>
<body>
<main class="stage">
  <section class="card card--front" aria-label="Card front">
    <span class="band band--left"></span>
    <span class="band band--right"></span>
    <div class="brand"><span class="brand__mark"></span>Halven Shingleworks</div>
  </section>

  <section class="card card--back" aria-label="Card back">
    <span class="band band--left"></span>
    <span class="band band--right"></span>
    <div class="brand"><span class="brand__mark"></span>Halven<br>Shingleworks</div>
    <span class="divider"></span>
    <div class="contact">
      <p class="contact__name"><span class="first">Tomas</span> Verrill</p>
      <p class="contact__role">Managing Director</p>
      <ul class="contact__list">
        <li>
          <svg viewBox="0 0 14 14" aria-hidden="true"><rect x="3" y="1" width="8" height="12" rx="1.5" fill="none" stroke="#232323" stroke-width="1.4"/><circle cx="7" cy="11" r="0.8" fill="#232323"/></svg>
          555 471 2086
        </li>
        <li>
          <svg viewBox="0 0 14 14" aria-hidden="true"><rect x="1" y="3" width="12" height="8" fill="#D62E22"/><path d="M1 3l6 5 6-5" fill="none" stroke="#fff" stroke-width="1.2"/></svg>
          support@halvenshingleworks.example
        </li>
        <li>
          <svg viewBox="0 0 14 14" aria-hidden="true"><circle cx="7" cy="7" r="5.8" fill="none" stroke="#D62E22" stroke-width="1.4"/><ellipse cx="7" cy="7" rx="2.4" ry="5.8" fill="none" stroke="#D62E22" stroke-width="1.1"/><path d="M1.2 7h11.6" stroke="#D62E22" stroke-width="1.1"/></svg>
          www.halvenshingleworks.example
        </li>
      </ul>
    </div>
  </section>
</main>
</body>
</html>
```